Web Design for an Innovative Life Science Marketplace

IMPORTANT:
The software is called CS-Cart. It has capabilities and limitations with design features in the software. There is a certain framework that needs to be followed. It is PHP and Linux. It may require add-ons for your design, so please be specific with what is required. It’s preferred the designer has CS-Cart knowledge/experience.

Key Requirements
1. I’d like the design to include an implemented/recommended CS-Cart theme that is consistent with our branding (see the marketing collateral and logo).
2. I then need the additional design changes to that theme to create the below web pages.
3. All designs should be consistent with our branding. All pictures should either be computer generated (clip art-like) or pictures of happy patients. What is a happy patient? Close up photo of someone healthy, happy, and experiencing/enjoying life. Not someone in a hospital or getting care. Please see examples already on the site.

Please see the attached Web Design details in the word document. That document is important to complete the design.

```html
<!DOCTYPE html>
<html lang="en">
<head>
<meta charset="utf-8">
<title>VERDALINK-QC — Quality Policy</title>
<link href="https://fonts.googleapis.com/css2?family=Raleway:wght@400;500;700;800&display=swap" rel="stylesheet">
<style>
  :root{
    --header-bg:#e4e5e4;
    --nav-text:#3f8f66;
    --nav-active:#8bc34a;
    --btn-teal:#1e7a6b;
    --btn-green:#8bc34a;
    --forest-dark:#17301f;
    --forest-mid:#2c4a2c;
    --panel-green:rgba(132,178,56,0.88);
    --panel-teal:rgba(30,122,107,0.88);
    --footer-bg:#1f7a6c;
    --footer-line:#7cbf3c;
    --title-green:#8bc34a;
    --title-faded:#9fb78a;
    --text-light:#ffffff;
    --photo-warm-a:#c9b9ad;
    --photo-warm-b:#8a8079;
    --photo-sky-a:#eef3f5;
    --photo-sky-b:#3fb2cf;
  }
  *{box-sizing:border-box;margin:0;padding:0}
  html,body{width:1200px;height:1200px;overflow:hidden}
  body{position:relative;font-family:'Raleway',sans-serif;color:var(--text-light);background:var(--forest-dark)}
  .forest-backdrop{position:absolute;left:0;top:38px;width:1200px;height:1052px;
    background:radial-gradient(ellipse at 50% 60%,#3a5a32 0%,var(--forest-mid) 45%,var(--forest-dark) 100%)}
  .site-header{position:absolute;left:0;top:0;width:1200px;height:38px;background:var(--header-bg)}
  .brand{position:absolute;left:158px;top:6px;font-weight:700;font-size:8.5px;color:var(--nav-text);white-space:nowrap}
  .main-nav a{position:absolute;top:5px;font-size:9px;letter-spacing:1.4px;color:var(--nav-text);text-decoration:none;white-space:nowrap}
  .main-nav a.is-active{color:var(--nav-active)}
  .account-btn{position:absolute;top:3px;height:11px;width:64px;border-radius:6px;font-size:8.5px;line-height:11px;text-align:center;color:#fff}
  .account-btn.login{left:910px;background:var(--btn-teal)}
  .account-btn.signup{left:985px;background:var(--btn-green)}
  .page-title{position:absolute;left:149px;top:37px;font-size:20px;font-weight:800;color:var(--title-green);letter-spacing:1.6px;white-space:nowrap}
  .page-title span{color:var(--title-faded)}
  .panel{position:absolute;overflow:hidden;font-size:14.6px;line-height:14.8px;letter-spacing:2.1px}
  .panel.green{background:var(--panel-green)}
  .panel.teal{background:var(--panel-teal)}
  .policy-panel{left:150px;top:62px;width:900px;height:252px;padding:5px 2px 0 38px}
  .intro-right{left:627px;top:328px;width:423px;height:266px;padding:31px 30px 0 26px}
  .intro-left{left:151px;top:602px;width:423px;height:267px;padding:11px 16px 0 34px}
  .closing-panel{left:150px;top:880px;width:900px;height:206px;padding:12px 16px 0 38px}
  .photo{position:absolute}
  .photo.baby{left:152px;top:328px;width:422px;height:266px;background:linear-gradient(135deg,var(--photo-warm-b),var(--photo-warm-a) 55%,#a59c95)}
  .photo.volunteers{left:626px;top:602px;width:423px;height:267px;background:radial-gradient(circle at 50% 50%,var(--photo-sky-a) 30%,var(--photo-sky-b) 85%)}
  .footer-line{position:absolute;left:0;top:1090px;width:1200px;height:3px;background:var(--footer-line)}
  .site-footer{position:absolute;left:0;top:1093px;width:1200px;height:107px;background:var(--footer-bg)}
  .footer-mark{position:absolute;left:156px;top:13px;width:18px;height:18px;border-radius:50%;background:#2e5a3a;border:2px solid #7cbf3c}
  .footer-brand{position:absolute;left:179px;top:24px;font-size:7.5px;font-weight:700;color:#fff;white-space:nowrap}
  .footer-links a,.legal-links a{position:absolute;font-size:7.2px;color:#fff;text-decoration:none;white-space:nowrap}
  .footer-links a{top:8px}
  .legal-links a{top:97px}
  .follow{position:absolute;left:186px;top:45px;font-size:14px;letter-spacing:.8px}
  .social{position:absolute;left:155px;top:66px;display:flex;gap:10px}
  .social span{width:27px;height:20px;border-radius:5px;background:#fff;opacity:.9}
  .contact{position:absolute;left:818px;top:42px;font-size:13px;line-height:19px;letter-spacing:.9px;white-space:nowrap}
  .contact div{display:flex;align-items:center;gap:8px}
</style>
</head>
<body>
  <div class="forest-backdrop" role="img" aria-label="Aerial photograph of a dense evergreen forest"></div>

  <header class="site-header">
    <div class="brand">VERDALINK-QC</div>
    <nav class="main-nav">
      <a class="is-active" href="#" style="left:231px">Home</a>
      <a href="#" style="left:302px">What We Do</a>
      <a href="#" style="left:418px">Who We Are</a>
      <a href="#" style="left:533px">Join Us</a>
      <a href="#" style="left:613px">Get In Touch</a>
    </nav>
    <a class="account-btn login">Login</a>
    <a class="account-btn signup">Sign up</a>
  </header>

  <h1 class="page-title">Quality <span>Policy</span></h1>

  <section class="panel green policy-panel">
    <p>Our Quality-Driven Firm<br>VERDALINK-QC is an innovative firm aspiring to solve waste and procurement problems within the life science supply chain while continuing to maintain the utmost compliance with industry and federal quality standards. Part 11 alignment, vetting of account owners and transactions, and robust GMP information for deals ensure all parties have the information and environment needed to source GMP or non-GMP material.</p>
    <p>Our Quality Commitment<br>VERDALINK-QC is fully committed to the quality of materials and safety of patients. As such, we provide oversight and regulation of the exchange to ensure transactions are transparent, traceable, compliant with the buyer's GMP requirements, and industry aligned.</p>
    <p>Our Quality Responsibility<br>VERDALINK-QC is fully entrusted and responsible for ensuring access to the exchange is restricted, non-conformance issues are investigated, and parties can seamlessly transact, make payments, and ship products in a professional and private venue for like-minded organizations aspiring to solve life-science waste problems.</p>
  </section>

  <div class="photo baby" role="img" aria-label="Photo of a happy baby wearing a flower crown on a soft blanket"></div>

  <section class="panel teal intro-right">
    <p>Lorem ipsum dolor sit amet, consectetur adipisicing elit, sed do eiusmod tempor incididunt ut labore et dolore magna aliqua. Ut enim ad minim veniam, quis nostrud exercitation ullamco laboris nisi ut aliquip ex ea commodo consequat. Duis aute irure dolor in reprehenderit in voluptate velit esse cillum dolore eu fugiat nulla pariatur. Excepteur sint occaecat cupidatat non proident, sunt in culpa qui officia deserunt mollit anim id est laborum. Sed ut perspiciatis unde omnis iste natus error sit voluptatem accusantium doloremque laudantium, totam rem</p>
  </section>

  <section class="panel green intro-left">
    <p>Lorem ipsum dolor sit amet, consectetur adipisicing elit, sed do eiusmod tempor incididunt ut labore et dolore magna aliqua. Ut enim ad minim veniam, quis nostrud exercitation ullamco laboris nisi ut aliquip ex ea commodo consequat. Duis aute irure dolor in reprehenderit in voluptate velit esse cillum dolore eu fugiat nulla pariatur. Excepteur sint occaecat cupidatat non proident, sunt in culpa qui officia deserunt mollit anim id est laborum. Sed ut perspiciatis unde omnis iste natus error sit voluptatem accusantium doloremque laudantium, totam rem aperiam, eaque ipsa quae ab illo inventore veritatis et quasi architecto beatae vitae dicta sunt</p>
  </section>

  <div class="photo volunteers" role="img" aria-label="Photo of four smiling volunteers in blue shirts looking down at the camera"></div>

  <section class="panel teal closing-panel">
    <p>Lorem ipsum dolor sit amet, consectetur adipisicing elit, sed do eiusmod tempor incididunt ut labore et dolore magna aliqua. Ut enim ad minim veniam, quis nostrud exercitation ullamco laboris nisi ut aliquip ex ea commodo consequat. Duis aute irure dolor in reprehenderit in voluptate velit esse cillum dolore eu fugiat nulla pariatur. Excepteur sint occaecat cupidatat non proident, sunt in culpa qui officia deserunt mollit anim id est laborum. Sed ut perspiciatis unde omnis iste natus error sit voluptatem accusantium doloremque laudantium, totam rem aperiam, eaque ipsa quae ab illo inventore veritatis et quasi architecto beatae vitae dicta sunt explicabo. Nemo enim ipsam voluptatem quia voluptas sit aspernatur aut odit aut fugit, sed quia consequuntur magni dolores eos qui ratione voluptatem sequi nesciunt. Neque porro quisquam est, qui dolorem ipsum quia dolor sit amet, consectetur, adipisci velit, sed quia non numquam eius modi tempora incidunt ut labore et dolore magnam aliquam quaerat voluptatem.</p>
  </section>

  <div class="footer-line"></div>
  <footer class="site-footer">
    <div class="footer-mark"></div>
    <div class="footer-brand">VERDALINK-QC</div>
    <nav class="footer-links">
      <a href="#" style="left:234px">Careers</a>
      <a href="#" style="left:295px">Contact</a>
      <a href="#" style="left:357px">News &amp; Press</a>
      <a href="#" style="left:442px">Privacy</a>
      <a href="#" style="left:501px">Policy</a>
      <a href="#" style="left:555px">Privacy Rights</a>
      <a href="#" style="left:641px">Login</a>
    </nav>
    <div class="follow">Follow</div>
    <div class="social" aria-label="Social media links"><span></span><span></span><span></span></div>
    <div class="contact">
      <div>
        <svg width="24" height="16" viewBox="0 0 24 16" fill="none" stroke="#fff" stroke-width="1.6"><rect x="1" y="1" width="22" height="14" rx="1.5"/><path d="M1 2l11 8 11-8"/></svg>
        <span>Email:info@verdalinkqc.com</span>
      </div>
      <div>
        <svg width="20" height="18" viewBox="0 0 24 24" fill="#fff"><path d="M6.6 10.8a15.1 15.1 0 0 0 6.6 6.6l2.2-2.2c.3-.3.7-.4 1-.2 1.1.4 2.3.6 3.6.6.6 0 1 .4 1 1V20c0 .6-.4 1-1 1A17 17 0 0 1 3 4c0-.6.4-1 1-1h3.5c.6 0 1 .4 1 1 0 1.3.2 2.5.6 3.6.1.3 0 .7-.2 1z"/></svg>
        <span>Phone:844-555-0142</span>
      </div>
    </div>
    <nav class="legal-links">
      <a href="#" style="left:510px">Site Terms</a>
      <a href="#" style="left:582px">State Disclosures</a>
      <a href="#" style="left:680px">Help</a>
    </nav>
  </footer>
</body>
</html>
```